Webdesign für Full-Service-Internetagentur
Zielgruppe
Brenntaler Webdesign – Ihr Partner für außergewöhnliche Onlinepräsenzen
Wir bieten seit mehr als 16 Jahren Internetauftritte für kleine und mittelständische Unternehmen an.
Als Full-Service-Internetagentur liefern wir Ihnen individuelle auf Ihre Bedürfnisse, Ihre Branche und Ihre Zielgruppe zugeschnittene Lösungen für Ihre Onlinepräsentation an. Unser Angebot beinhaltet sowohl ein ideenreiches Webdesign kombiniert mit den aktuellsten Grundsätzen für Web-Programmierung als auch die Unterstützung für Ihr erfolgreiches Werben im Internet.
Eine gute Beratung heißt für uns genau hinhören und verstehen, was Sie wirklich brauchen. Je besser wir Ihre Ziele kennen, desto besser können wir Ihre Onlinepräsenz umsetzen. Unsere Kundenberater erläutern Ihnen persönlich mit Enthusiasmus die verschiedenen Möglichkeiten der Darstellung Ihrer Firma im Internet und entwickeln Konzepte, die Ihren Anforderungen bestmöglich entsprechen. Nicht nur während der Projektphase, sondern auch nach Onlinestellung Ihrer Internetseite stehen wir Ihnen mit persönlicher Kundenbetreuung und Supportdienstleistungen zur Verfügung.
Aufgabenstellung
siehe : https://www.brenntaler-webdesign.de/

```html
<!DOCTYPE html>
<html lang="de">
<head>
<meta charset="utf-8">
<title>Brenntaler Webdesign – Ihr Partner für außergewöhnliche Onlinepräsenzen</title>
<link href="https://fonts.googleapis.com/css2?family=Roboto:wght@400;500;700&family=Montserrat:wght@500;600&family=Ubuntu:wght@400;500&display=swap" rel="stylesheet">
<style>
:root{
  --red:#e3141b;
  --dark:#222;
  --text:#444;
  --muted:#777;
  --outer:#ededed;
  --light:#f6f6f8;
  --blush:#fdf1ef;
  --line:#ddd;
}
*{box-sizing:border-box;margin:0;padding:0}
html,body{width:1200px;height:2841px;overflow:hidden}
body{background:var(--outer);font-family:Roboto,Arial,sans-serif;color:var(--text);position:relative}
.page{position:absolute;left:54px;top:6px;width:1091px;height:2835px;background:#fff;overflow:hidden}
.abs{position:absolute}
.btn{position:absolute;display:flex;align-items:center;justify-content:center;border-radius:20px;font-size:9px;font-weight:700;text-transform:uppercase;color:var(--dark);border:1.5px solid var(--dark);background:#fff}
.btn.red{background:var(--red);border-color:var(--red);color:#fff}
.btn.red-outline{border-color:var(--red);color:var(--red)}
.logo{font-family:Ubuntu,sans-serif;font-size:19px;font-weight:400;color:var(--dark);line-height:1}
.nav a{position:absolute;top:36px;font-size:8.5px;font-weight:700;color:var(--dark);text-decoration:none}
.nav a.active{border-bottom:1.5px solid var(--red);padding-bottom:4px}
.badge{position:absolute;background:#b81c22;border-radius:2px}
.badge::before{content:"";position:absolute;left:0;right:0;top:0;height:38%;background:#f2f2f2}
.media{position:absolute}
h1{font-size:26px;font-weight:700;color:var(--dark);line-height:32px}
.service{position:absolute;width:180px;text-align:center}
.service .ic{width:72px;height:72px;margin:0 auto 20px;border-radius:12px;background:linear-gradient(135deg,#ffd24d,#3fa0e8 55%,#e9433a)}
.service h3{font-size:11px;font-weight:700;color:var(--dark);margin-bottom:8px}
.service p{font-size:9px;line-height:14px;color:#555}
.field{position:absolute;background:rgba(255,255,255,.75);border:1px solid #ddd;font-size:8px;color:#888;padding:9px 10px}
.news{position:absolute;border:1px solid #e4e4e4;background:#fff;padding:22px 21px}
.news .meta{font-size:8px;color:#999;white-space:nowrap}
.news .meta b{color:var(--red);font-weight:400;margin-left:8px}
.news h4{font-family:Montserrat,sans-serif;font-size:11px;font-weight:600;color:var(--dark);margin:8px 0 3px;line-height:14px}
.news p{font-size:7.5px;color:#444}
.news .more{font-size:8px;font-weight:500;color:#555;margin-top:17px}
.foot h5{font-size:9px;font-weight:500;color:var(--red);margin-bottom:10px}
.foot p{font-size:8.5px;line-height:12px;color:#333}
.dots span{display:inline-block;width:6px;height:6px;border-radius:50%;background:#dde;margin-right:3px}
.dots span.on{background:var(--red)}
</style>
</head>
<body>
<div class="page">

  <!-- header -->
  <div class="abs logo" style="left:206px;top:32px">Brenntaler Webdesign</div>
  <nav class="nav">
    <a class="active" style="left:449px" href="#">DIE AGENTUR</a>
    <a style="left:519px" href="#">REFERENZEN</a>
    <a style="left:583px" href="#">ENGAGEMENT</a>
    <a style="left:653px" href="#">AKTUELLES</a>
    <a style="left:712px" href="#">KONTAKT</a>
    <a style="left:761px" href="#">FAQ</a>
  </nav>
  <div class="btn red-outline" style="left:791px;top:27px;width:98px;height:27px">Projekt starten</div>
  <div class="badge" style="left:1024px;top:64px;width:67px;height:88px" aria-label="Partner-Siegel"></div>

  <!-- hero -->
  <svg class="media" style="left:576px;top:62px" width="486" height="440" viewBox="0 0 486 440" role="img" aria-label="Foto: Frau arbeitet lächelnd am Laptop">
    <defs><linearGradient id="hg" x1="0" y1="0" x2="1" y2="1"><stop offset="0" stop-color="#d9c8b8"/><stop offset=".55" stop-color="#b8a89a"/><stop offset="1" stop-color="#8d8580"/></linearGradient></defs>
    <path d="M170 20C230-10 300 10 340 60C380 110 440 120 470 180C500 250 470 330 420 380C360 440 240 450 140 430C50 410 0 380 2 300C5 220 40 180 70 130C100 80 120 45 170 20Z" fill="url(#hg)"/>
  </svg>
  <div class="abs" style="left:206px;top:175px;font-size:18px;color:var(--dark)">Brenntaler Webdesign</div>
  <h1 class="abs" style="left:206px;top:197px;width:400px">Ihr Partner für außergewöhnliche Onlinepräsenzen</h1>
  <p class="abs" style="left:207px;top:270px;width:360px;font-size:11px;line-height:17px;color:#333">Wir bieten seit mehr als 16 Jahren Internetauftritte für kleine und mittelständische Unternehmen an.</p>
  <div class="btn red" style="left:207px;top:338px;width:111px;height:31px">Projekt starten</div>
  <div class="btn" style="left:323px;top:338px;width:113px;height:31px">Weiterlesen</div>

  <!-- services with wave -->
  <svg class="media" style="left:0;top:760px" width="1091" height="260" viewBox="0 0 1091 260">
    <path d="M0 60C200 140 380 210 560 205C760 200 930 110 1091 0V260H0Z" fill="var(--light)"/>
  </svg>
  <div class="abs" style="left:0;top:583px;width:1091px;text-align:center;font-size:14px;color:var(--dark)">Wir bieten Lösungen<br><b style="font-size:16px;line-height:22px">die von unseren Nutzern geliebt werden</b></div>
  <div class="service" style="left:178px;top:664px"><div class="ic" role="img" aria-label="Illustration Konzeption"></div><h3>Konzeption &amp; Beratung</h3><p>Wir entwickeln Ihr individuelles Konzept und begleiten Sie über die Fertigstellung hinaus.</p></div>
  <div class="service" style="left:371px;top:664px"><div class="ic" role="img" aria-label="Illustration Programmierung"></div><h3>Webdesign &amp; Programmierung</h3><p>Wir setzen Ihre individuell gestaltete Webseite mittels aktueller Web-Technologien um.</p></div>
  <div class="service" style="left:576px;top:664px"><div class="ic" role="img" aria-label="Illustration Suchmaschinenoptimierung"></div><h3>SEO &amp; Online Marketing</h3><p>Wir analysieren Ihre Webseite und schaffen Voraussetzungen für ein optimales Such-Ranking.</p></div>
  <div class="service" style="left:780px;top:664px"><div class="ic" role="img" aria-label="Illustration Hosting"></div><h3>Domain &amp; Webhosting</h3><p>Alles was Sie für Ihr Webprojekt brauchen.</p></div>
  <div class="abs" style="left:456px;top:855px;width:145px;height:34px;border:1.5px solid var(--red);border-radius:18px;background:#fff;text-align:center;padding-top:4px;font-size:9px;color:var(--dark);line-height:10px">Sie einen Termin unter<br><b style="color:var(--red);font-size:13px;line-height:16px">0361 4472190</b></div>

  <!-- about -->
  <div class="abs" style="left:0;top:1000px;width:1091px;height:120px;background:var(--light)"></div>
  <svg class="media" style="left:0;top:1080px" width="1091" height="350" viewBox="0 0 1091 350">
    <path d="M0 0H1091V240C900 250 760 170 560 260C360 350 150 340 0 270Z" fill="var(--blush)"/>
  </svg>
  <svg class="media" style="left:208px;top:1014px" width="382" height="344" viewBox="0 0 382 344" role="img" aria-label="Teamfoto: vier Mitarbeitende in weißen Hemden">
    <defs><linearGradient id="tg" x1="0" y1="0" x2="1" y2="1"><stop offset="0" stop-color="#d6d6d6"/><stop offset=".5" stop-color="#ececec"/><stop offset="1" stop-color="#c8c0ba"/></linearGradient></defs>
    <path d="M60 20C130-5 230-5 300 30C360 60 385 120 370 170C350 220 250 230 190 290C150 330 100 350 50 330C10 310 0 250 2 190C5 120 10 45 60 20Z" fill="url(#tg)"/>
  </svg>
  <div class="abs" style="left:606px;top:1067px;font-size:9.5px;color:var(--red)">Ehrlich. Streßerprobt. Verständlich. Erfolgreich.</div>
  <h2 class="abs" style="left:606px;top:1080px;width:300px;font-size:20px;line-height:23px;font-weight:500;color:var(--dark)">Erfrischendes und kreatives Webdesign</h2>
  <p class="abs" style="left:606px;top:1136px;width:285px;font-size:9.5px;line-height:14.5px;color:#333">Unsere Leistungen sind transparent und die Projektkosten sind realistisch. Wir versprechen nicht zu viel und verschweigen auch nicht potentielle Ecken und Kanten. Online wie offline ist vieles möglich, aber längst nicht alles ist sinnvoll.</p>
  <div class="btn" style="left:607px;top:1213px;width:89px;height:25px;font-size:8px">Weiterlesen</div>

  <!-- references -->
  <h2 class="abs" style="left:206px;top:1476px;font-size:20px;font-weight:500;color:var(--dark)">Referenzen</h2>
  <div class="abs" style="left:206px;top:1505px;font-size:9.5px;color:#333">Eine Auswahl unserer abgeschlossenen Projekte aus unserem Portfolio</div>
  <div class="btn" style="left:798px;top:1486px;width:90px;height:27px;font-size:8px">Alles sehen</div>
  <div class="abs" style="left:207px;top:1549px;width:681px;height:270px;background:linear-gradient(90deg,#fff 40%,var(--blush))"></div>
  <div class="media" style="left:207px;top:1549px;width:280px;height:270px;background:linear-gradient(160deg,#e9e4df,#c9c1b8 50%,#9a3a35)" role="img" aria-label="Bildschirmansicht der Referenz-Webseite Kovar Bauunternehmen"></div>
  <div class="abs" style="left:515px;top:1597px;font-size:7.5px;color:#999">▭ &nbsp;WEBDESIGN &amp; PROGRAMMIERUNG</div>
  <div class="abs" style="left:515px;top:1627px;font-size:14px;font-weight:500;color:var(--dark)">Kovar Bauunternehmen</div>
  <p class="abs" style="left:515px;top:1651px;width:345px;font-size:9.5px;line-height:14px;color:#333">Lorem ipsum dolor sit amet, consectetur adipiscing elit, sed do eiusmod tempor incididunt ut labore et dolore magna aliqua. Ut enim ad minim veniam, quis nostrud exercitation ullamco laboris nisi ut aliquip ex ea commodo consequat. Duis aute irure dolor in reprehenderit in voluptate velit esse cillum dolore eu fugiat nulla</p>
  <div class="btn red" style="left:517px;top:1733px;width:88px;height:24px;font-size:8px">Live Vorschau</div>
  <div class="abs dots" style="left:531px;top:1783px"><span></span><span></span><span class="on"></span><span></span></div>

  <!-- news -->
  <h2 class="abs" style="left:0;top:1873px;width:1091px;text-align:center;font-size:19px;font-weight:500;color:var(--dark)">WAS ES NEUES GIBT</h2>
  <div class="abs" style="left:213px;top:1924px;width:327px;height:245px;background:#fff;box-shadow:0 2px 8px rgba(0,0,0,.15)">
    <div style="height:24px;padding:6px 8px;font-size:9px;color:#333">Dellentechnik Morand</div>
    <div style="height:163px;background:linear-gradient(180deg,#c8b79a,#27a6b5 45%,#1e7f92)" role="img" aria-label="Foto: Firmengebäude mit Transporter"></div>
    <div style="background:#f3f3f3;height:58px;text-align:center;padding-top:14px">
      <div style="font-size:12px;color:#7bb82d">DELLENTECHNIK MORAND</div>
      <div style="font-size:7px;color:#999;margin-top:3px">Wir beseitigen professionell Dellen, Kratzer und Hagelschäden!</div>
    </div>
  </div>
  <div class="news" style="left:564px;top:1924px;width:325px;height:114px">
    <div class="meta">▤ JULI 06, 2019 &nbsp;|<b>Website sich an Smartphone- und Tablet-Bildschirmgrößen</b></div>
    <h4>Malerprojekt Brenntal GmbH</h4>
    <p>Neue Website für die Malerprojekt Brenntal GmbH</p>
    <div class="more">Weiterlesen →</div>
  </div>
  <div class="news" style="left:564px;top:2054px;width:325px;height:114px">
    <div class="meta">▤ JANUAR 16, 2019 &nbsp;|<b>mailcloud</b></div>
    <h4>ACHTUNG – eingeschränkten Verfügbarkeit von MailCloud-Konten</h4>
    <p>Aktuelle Systemmeldungen HostingWerk</p>
    <div class="more" style="margin-top:13px">Weiterlesen →</div>
  </div>
  <div class="btn" style="left:499px;top:2202px;width:124px;height:26px;font-size:7.5px">Alle Beiträge anzeigen</div>

  <!-- contact -->
  <div class="media" style="left:0;top:2264px;width:554px;height:414px;background:linear-gradient(160deg,#e6e6e6,#cfcfcf 60%,#b9b9b9)" role="img" aria-label="Foto: Hände auf einer Tastatur"></div>
  <div class="media" style="left:554px;top:2264px;width:537px;height:414px;background:linear-gradient(135deg,#eef0f2,#e3ebe1 60%,#d9e9cf)" role="img" aria-label="Lageplan mit Standortmarkierung der Agentur"></div>
  <div class="abs" style="left:207px;top:2304px;font-size:17px;color:var(--dark)">Wir haben Ihr Interesse geweckt?</div>
  <div class="field" style="left:207px;top:2369px;width:160px;height:28px">Name *</div>
  <div class="field" style="left:377px;top:2369px;width:160px;height:28px">Firma</div>
  <div class="field" style="left:207px;top:2403px;width:160px;height:28px">Straße, Nr.</div>
  <div class="field" style="left:377px;top:2403px;width:160px;height:28px">PLZ, Ort</div>
  <div class="field" style="left:207px;top:2437px;width:160px;height:28px">Telefon *</div>
  <div class="field" style="left:377px;top:2437px;width:160px;height:28px">E-Mail *</div>
  <div class="field" style="left:207px;top:2471px;width:330px;height:74px">Ihre Nachricht an uns *</div>
  <div class="abs" style="left:209px;top:2553px;width:15px;height:13px;background:#fff;border:1px solid #ddd"></div>
  <p class="abs" style="left:233px;top:2570px;width:305px;font-size:7px;line-height:12px;color:#333">Ich habe die Datenschutzerklärung zur Kenntnis genommen. Ich stimme zu, dass meine Angaben und Daten zur Beantwortung meiner Anfrage elektronisch erhoben und gespeichert werden. Hinweis: Sie können Ihre Einwilligung jederzeit für die Zukunft per E-Mail an <span style="color:var(--red)">info@brenntaler-webdesign.de</span> widerrufen.</p>
  <div class="btn red" style="left:207px;top:2628px;width:114px;height:24px;font-size:7.5px">Formular abschicken</div>

  <!-- footer -->
  <div class="abs foot" style="left:206px;top:2700px">
    <h5>NAVIGATION</h5>
    <p style="position:absolute;top:20px;left:0;line-height:17px;width:60px">Portfolio<br>Die Agentur<br>Referenzen<br>Aktuelles</p>
    <p style="position:absolute;top:20px;left:77px;line-height:17px;width:70px">Kontakt<br>FAQ<br>Impressum<br>Datenschutz</p>
  </div>
  <div class="abs foot" style="left:451px;top:2700px;width:300px">
    <h5>KONTAKT</h5>
    <p>Brenntaler Webdesign<br>Inh. Lena Hartwig<br>Lindenhofer Straße 12<br>07743 Brenntal</p>
    <p style="position:absolute;left:137px;top:21px;width:160px">Fon: 0361 - 4472190<br>Fax: 0361 - 4472199<br>info@brenntaler-webdesign.de</p>
  </div>
  <div class="badge" style="left:820px;top:2694px;width:69px;height:88px" aria-label="Partner-Siegel"></div>
  <div class="abs" style="left:0;top:2796px;width:1091px;height:39px;background:#eee;text-align:center;padding-top:12px;font-size:8px;color:#333">© 2019 by <span style="color:var(--red)">Brenntaler Webdesign</span></div>
</div>
</body>
</html>
```